A design led business card for the construction industry

High-end business card to match logo. White logo on dark grey/off black to the front. Matching dark font on white to back, possibly with logo design again.

We offer construction and project management services to commercial and private clients in the UK. Projetcs range from newbuilds, conversion of listed buildings and refurbishments and extensions of existing homes. Our focus is on quality and attention to detail using the highest skills.

Contact Information for Business Card

Name; Dorian Hatch BSc
Position; Project Manager
Mobile; 07962 804 157
Tel; 01632 958412
email; dorian@framelark.co.uk
web; www.framelark.co.uk
Address; Ashcombe Vale, KT4 7PZ

Colors

Designer to choose only greyscale colors for use in the design.

Requirements
Must have
• To include the below description of the business,

CONSTRUCTION - PROJECT MANAGEMENT
Nice to have
• The posibility of the top back of the card being used as a ruler. So will have a measurement to scale in mm or an architect scale of 1:50
Should not have
• Should not be portrait

```html
<!DOCTYPE html>
<html lang="en">
<head>
<meta charset="utf-8">
<title>Framelark business card</title>
<link href="https://fonts.googleapis.com/css2?family=Arimo:wght@400;700&display=swap" rel="stylesheet">
<style>
  :root {
    --backdrop: #262626;
    --card: #0b0b0b;
    --ink: #f4f4f4;
    --rule: #5a5a5a;
  }
  * { box-sizing: border-box; margin: 0; padding: 0; }
  html, body {
    width: 1200px; height: 900px; overflow: hidden;
    background: var(--backdrop);
    font-family: "Arimo", Arial, sans-serif;
    color: var(--ink);
  }
  .stage {
    width: 1200px; height: 900px;
    display: flex; align-items: center; justify-content: center; gap: 40px;
  }
  .card {
    width: 560px; height: 320px;
    background: var(--card);
    position: relative;
    box-shadow: 0 10px 30px rgba(0,0,0,.45);
  }

  /* contact side */
  .card--contact { display: flex; align-items: center; }
  .brand-block {
    width: 270px; display: flex; flex-direction: column; align-items: center; gap: 18px;
  }
  .brand-square {
    width: 110px; height: 110px; border: 4px solid var(--ink);
  }
  .wordmark {
    font-size: 19px; font-weight: 400; letter-spacing: 9px; padding-left: 9px;
  }
  .divider {
    width: 1px; height: 170px; background: var(--rule);
  }
  .contact-block { padding-left: 28px; }
  .contact-name { font-size: 17px; font-weight: 700; text-transform: uppercase; }
  .contact-name .credential { font-weight: 400; text-transform: none; }
  .contact-role { font-size: 13px; margin: 2px 0 14px; }
  .contact-list { list-style: none; font-size: 13px; line-height: 19px; }
  .contact-list li { display: flex; align-items: center; gap: 8px; }
  .contact-list svg { width: 12px; height: 12px; flex: none; }
  .contact-address { font-size: 13px; margin-top: 14px; }

  /* logo side */
  .card--front {
    display: flex; flex-direction: column; align-items: center; justify-content: center; gap: 18px;
  }
  .card--front .brand-square { width: 130px; height: 130px; }
  .card--front .wordmark { font-size: 22px; letter-spacing: 11px; padding-left: 11px; }
  .tagline { font-size: 12px; letter-spacing: .5px; }
</style>
</head>
<body>
<main class="stage">
  <section class="card card--contact">
    <div class="brand-block">
      <div class="brand-square"></div>
      <div class="wordmark">FRAMELARK</div>
    </div>
    <div class="divider"></div>
    <div class="contact-block">
      <p class="contact-name">Dorian Hatch <span class="credential">BSc</span></p>
      <p class="contact-role">Project Manager</p>
      <ul class="contact-list">
        <li>
          <svg viewBox="0 0 12 12" fill="none" stroke="currentColor" stroke-width="1.2"><rect x="3" y="0.8" width="6" height="10.4" rx="1"/><line x1="5" y1="9.5" x2="7" y2="9.5"/></svg>
          07962 804 157
        </li>
        <li>
          <svg viewBox="0 0 12 12" fill="currentColor"><path d="M2.5 1l2 2.2-1 1.3c.7 1.5 1.7 2.5 3.1 3.2l1.3-1 2.1 2-1 1.8C5.2 10.2 1.6 6.7 1 1.9z"/></svg>
          01632 958412
        </li>
        <li>
          <svg viewBox="0 0 12 12" fill="none" stroke="currentColor" stroke-width="1.2"><rect x="0.8" y="2.5" width="10.4" height="7"/><polyline points="0.8,2.5 6,6.5 11.2,2.5"/></svg>
          dorian@framelark.co.uk
        </li>
        <li>
          <svg viewBox="0 0 12 12" fill="none" stroke="currentColor" stroke-width="1"><circle cx="6" cy="6" r="5"/><ellipse cx="6" cy="6" rx="2.2" ry="5"/><line x1="1" y1="6" x2="11" y2="6"/></svg>
          www.framelark.co.uk
        </li>
      </ul>
      <p class="contact-address">Ashcombe Vale, KT4 7PZ</p>
    </div>
  </section>

  <section class="card card--front">
    <div class="brand-square"></div>
    <div class="wordmark">FRAMELARK</div>
    <p class="tagline">CONSTRUCTION - PROJECT MANAGEMENT</p>
  </section>
</main>
</body>
</html>
```